Infographic for council approvals process

Looking to show the different steps that a person needs to undertake to get local council approval for their new swimming pool. It's a bit convoluted and text heavy when written out, but could be more graphically illustrated as a series of steps and choices.
Needs to be aligned to the brand for www.LagoonBuildPacksOnline.com.au

Target Market(s)

Home Owners

Font styles to use
Sans Serif

Requirements
Must have
• Nice graphics that help simplify and layout the process graphically, the infographic should reference our brand colours and logos.

```html
<!DOCTYPE html>
<html lang="en">
<head>
<meta charset="utf-8">
<title>Council Approval for a New Swimming Pool – Lagoon Build Packs Online</title>
<link href="https://fonts.googleapis.com/css2?family=Montserrat:wght@700;800;900&family=Inter:wght@400;600;700&display=swap" rel="stylesheet">
<style>
:root{
  --bg:#dcf2f8;
  --navy:#0d3a5a;
  --teal:#74cdcf;
  --teal-soft:#a6e0e1;
  --pale:#e4f6f7;
  --cyan:#19a9e1;
  --yellow:#f4c430;
  --white:#ffffff;
}
*{box-sizing:border-box;margin:0;padding:0}
html,body{width:1200px;height:675px;overflow:hidden;background:var(--bg)}
body{font-family:"Inter",sans-serif;color:var(--navy);position:relative}
.abs{position:absolute}

/* title */
.kicker{left:467px;top:71px;width:652px;display:flex;align-items:center;gap:10px;font-family:"Montserrat",sans-serif;font-weight:800;font-size:16px;letter-spacing:1px;color:var(--teal)}
.kicker::before,.kicker::after{content:"";flex:1;height:1px;background:var(--teal)}
.main-title{left:466px;top:92px;width:654px;font-family:"Montserrat",sans-serif;font-weight:900;font-size:16.6px;letter-spacing:1px;color:var(--navy);white-space:nowrap;text-align:center}

/* panels */
.panel{position:absolute;font-size:5.1px;line-height:1.3}
.panel h3{font-size:6.4px;font-weight:700;margin-bottom:6px}
.panel p{text-align:justify}
.navy-panel{background:var(--navy);color:var(--white)}
.teal-panel{background:var(--teal);color:var(--white)}

.step1{left:195px;top:114px;width:216px;height:125px;border-radius:26px 0 0 0;padding:48px 12px 0 13px;box-shadow:7px 0 0 var(--teal-soft)}
.step1 h3{color:var(--teal-soft)}
.tips{left:37px;top:264px;width:216px;height:215px;border-radius:0 0 0 28px;padding:11px 13px 0 13px}
.tips h3{color:var(--white)}
.tips ol{list-style:none}
.tips li{display:flex;gap:6px;margin-bottom:4px}
.tips li span.n{flex:none;width:7px;height:7px;border-radius:50%;background:var(--navy);color:var(--white);font-size:3.4px;display:flex;align-items:center;justify-content:center;margin-top:1px}
.tips li p{color:var(--navy)}
.tips-band{left:37px;top:257px;width:276px;height:7px;background:var(--navy)}
.spine{left:271px;top:262px;width:6px;height:299px;background:var(--navy)}

.step2{left:436px;top:181px;width:216px;height:214px;border-radius:30px 30px 0 0;padding:49px 12px 0 12px}
.step2 > h3{color:var(--white)}
.step2 > p{color:var(--navy)}
.options{display:flex;gap:7px;margin-top:9px}
.opt{flex:1}
.opt-head{background:var(--navy);color:var(--white);font-weight:700;font-size:6.6px;letter-spacing:1px;text-align:center;padding:4px 0}
.opt-body{background:var(--white);color:var(--navy);height:98px;padding:5px 8px;font-size:4.6px;line-height:1.28;overflow:hidden}
.docs{top:181px;width:216px;height:214px;border-radius:30px 30px 0 0;padding:52px 12px 0 15px;font-size:4.6px;line-height:1.28}
.docs h3{color:var(--white);font-size:7.4px;margin-bottom:5px}
.docs ol{padding-left:7px;color:var(--navy)}
.docs li{margin-bottom:2px}
.cdc{left:681px}
.da{left:926px}
.note{position:absolute;left:12px;right:12px;top:190px;background:var(--white);color:var(--navy);padding:3px 4px}
.base-bar{left:400px;top:395px;width:741px;height:7px;background:var(--navy)}
.flow-arrow{top:278px;width:30px;height:22px}

.step3{left:278px;top:436px;width:216px;height:125px;border-radius:0 0 30px 0;padding:10px 12px 0 13px}
.step3 h3{color:var(--teal-soft)}

/* brand disc */
.brand{left:263px;top:257px;width:162px;height:162px;border-radius:50%;background:var(--white);border:5px solid var(--teal);box-shadow:0 0 0 4px var(--white);display:flex;align-items:center;justify-content:center;text-align:center}
.brand-name{font-family:"Montserrat",sans-serif;font-weight:800;font-size:13px;line-height:1.2;color:var(--navy);letter-spacing:.4px}

.num{position:absolute;width:28px;height:28px;border-radius:50%;background:var(--navy);border:2px solid var(--teal-soft);color:var(--white);font-family:"Montserrat",sans-serif;font-weight:800;font-size:12px;display:flex;align-items:center;justify-content:center}
.num.on-navy{background:var(--navy);box-shadow:0 0 0 2px var(--navy)}

/* badges */
.badge{position:absolute;width:84px;height:84px}
.badge svg{position:absolute;inset:0}
.badge-label{position:absolute;left:0;right:0;top:44px;text-align:center;color:var(--white);font-weight:700;font-size:7.6px;line-height:1.25}

/* guidelines table */
.tab{top:417px;height:19px;display:flex;align-items:center;justify-content:center;font-weight:700;font-size:8.5px;color:var(--white)}
.tab-nsw{left:717px;width:116px;background:var(--cyan);border-radius:14px 0 0 0}
.tab-guide{left:833px;width:115px;background:var(--yellow);color:var(--navy);border-radius:0 14px 0 0;font-size:8px}
.grid{left:523px;width:618px;display:grid;grid-template-columns:repeat(8,1fr)}
.row-a{top:436px}
.row-b{top:499px}
.cell{display:flex;align-items:center;justify-content:center;text-align:center;font-size:4.1px;line-height:1.25;font-weight:600;padding:0 3px;position:relative}
.lbl{height:28px}
.val{height:30px;font-size:4px}
.row-b .val{height:58px}
.c-t{background:var(--teal);color:var(--navy)}
.c-n{background:var(--navy);color:var(--white)}
.lbl::after{content:"";position:absolute;bottom:-3px;left:50%;margin-left:-4px;border-left:4px solid transparent;border-right:4px solid transparent;border-top:5px solid var(--yellow);z-index:2}
.yellow-arrow{left:494px;top:475px;width:52px;height:41px}
.return-line{left:1141px;top:463px;width:22px;height:64px}
</style>
</head>
<body>

<svg width="0" height="0" style="position:absolute">
  <defs>
    <polygon id="scallop" points="82,42 76.8,51.3 76.6,62 67.5,67.5 62,76.6 51.3,76.8 42,82 32.7,76.8 22,76.6 16.5,67.5 7.4,62 7.2,51.3 2,42 7.2,32.7 7.4,22 16.5,16.5 22,7.4 32.7,7.2 42,2 51.3,7.2 62,7.4 67.5,16.5 76.6,22 76.8,32.7"/>
    <clipPath id="inner"><circle cx="42" cy="42" r="31"/></clipPath>
    <g id="badge-base">
      <use href="#scallop" fill="var(--pale)" stroke="var(--pale)" stroke-width="6" stroke-linejoin="round"/>
      <use href="#scallop" fill="none" stroke="var(--teal)" stroke-width="1.5" stroke-linejoin="round" transform="translate(4.2 4.2) scale(.9)"/>
      <g clip-path="url(#inner)">
        <rect x="0" y="0" width="84" height="84" fill="var(--pale)"/>
        <rect x="0" y="38" width="84" height="50" fill="var(--navy)"/>
      </g>
      <path d="M36 72 l6 4 l6 -4" fill="none" stroke="var(--teal)" stroke-width="1.6"/>
    </g>
    <g id="badge-doc">
      <use href="#scallop" fill="var(--pale)" stroke="var(--pale)" stroke-width="6" stroke-linejoin="round"/>
      <circle cx="42" cy="42" r="33" fill="var(--white)" stroke="var(--navy)" stroke-width="4"/>
      <rect x="34" y="23" width="22" height="30" rx="2" fill="var(--teal)" transform="rotate(8 45 38)"/>
      <rect x="27" y="25" width="23" height="32" rx="2" fill="var(--cyan)"/>
      <g stroke="var(--white)" stroke-width="1.6"><line x1="31" y1="33" x2="46" y2="33"/><line x1="31" y1="38" x2="46" y2="38"/><line x1="31" y1="43" x2="46" y2="43"/><line x1="31" y1="48" x2="42" y2="48"/></g>
    </g>
  </defs>
</svg>

<div class="abs kicker">PROCESS STEP FOR</div>
<h1 class="abs main-title">LOCAL COUNCIL APPROVAL FOR THEIR NEW SWIMMING POOL</h1>

<div class="abs tips-band"></div>
<div class="abs spine"></div>

<section class="panel navy-panel step1">
  <h3>What do I need to do to get my pool approved?</h3>
  <p>Navigating the planning requirements for installing a swimming pool can be a complex process, varying significantly across different Australian states. In New South Wales (NSW), Queensland (QLD), Victoria (VIC), and the Australian Capital Territory (ACT), understanding the specific regulations and procedures is crucial for a successful project. Each state has its own approval process, required permits, compliance standards, and inspection procedures.</p>
</section>
<div class="num on-navy" style="left:208px;top:125px">01</div>
<div class="badge" style="left:261px;top:67px">
  <svg viewBox="0 0 84 84"><use href="#badge-base"/><circle cx="42" cy="27" r="8" fill="none" stroke="var(--navy)" stroke-width="2"/><path d="M38 27 l3 3 l7 -8" fill="none" stroke="var(--navy)" stroke-width="2.2"/></svg>
  <div class="badge-label">Pool<br>Approved</div>
</div>

<section class="panel teal-panel tips">
  <h3>Tips for Successfully Navigating Planning Requirements</h3>
  <ol>
    <li><span class="n">01</span><p>Thoroughly research and understand local regulations. Take the time to familiarise yourself with the specific planning requirements in your area to ensure compliance. It's always best to have a clear roadmap a the beginning of what is required. A checklist is a great way to track the process.</p></li>
    <li><span class="n">02</span><p>Seek professional guidance when needed. If you encounter complexities or uncertainties in the planning process, don't hesitate to consult with professionals. There are aspects of the approval process that can be quite daunting, especially if your site has certain additional regulation requirements due to soil type or flood plain issues. Sometimes it's best to use a professional service that can take care of the approval process for you.</p></li>
    <li><span class="n">03</span><p>Complete all necessary paperwork accurately and on time. Ensure that you submit all required documentation promptly and accurately, as delays or errors in paperwork can prolong the approval process.</p></li>
    <li><span class="n">04</span><p>Stay informed about any updates or changes to regulations. The regulations can change so keep in touch with your local Council to ensure your application is up to date with the latest standards.</p></li>
  </ol>
</section>
<div class="num" style="left:212px;top:441px">04</div>
<div class="badge" style="left:103px;top:436px">
  <svg viewBox="0 0 84 84"><use href="#badge-base"/><circle cx="42" cy="26" r="5" fill="none" stroke="var(--teal)" stroke-width="1.6"/><line x1="40" y1="32" x2="44" y2="32" stroke="var(--teal)" stroke-width="1.6"/><g stroke="var(--teal)" stroke-width="1.2"><line x1="42" y1="16" x2="42" y2="18"/><line x1="33" y1="26" x2="35" y2="26"/><line x1="49" y1="26" x2="51" y2="26"/><line x1="35.5" y1="19.5" x2="37" y2="21"/><line x1="48.5" y1="19.5" x2="47" y2="21"/></g></svg>
  <div class="badge-label">Tips for<br>Navigating</div>
</div>

<div class="abs brand"><div class="brand-name">LAGOON BUILD<br>PACKS ONLINE</div></div>

<section class="panel teal-panel step2">
  <h3>Council Approval for a Pool in NSW</h3>
  <p>In NSW, every new pool construction must receive approval from a Licensed Certifier. Depending on the specific circumstances, some pools may need a Complying Development (CDC), while others will need a Development Application (DA) approval from the council.</p>
  <div class="options">
    <div class="opt"><div class="opt-head">OPTION 1: CDC</div><div class="opt-body">Most customers prefer to apply for a CDC as it is a faster, cheaper and straight forward process with a private certifier instead of the local council. In order to apply for a CDC, certain criteria need to be met. Make sure you look at this criteria to ensure you are eligible.</div></div>
    <div class="opt"><div class="opt-head">Option 2: DA</div><div class="opt-body">If you don't meet the requirements for a CDC, you'll need to obtain development consent from your local Council by submitting a Development Application (DA). This is the sole approval pathway in certain scenarios, such as if you're building a new home. Unfortunately this is a longer and more expensive process so make sure you get this underway as soon as possible.</div></div>
  </div>
</section>
<div class="num" style="left:448px;top:191px">02</div>
<div class="badge" style="left:502px;top:139px">
  <svg viewBox="0 0 84 84"><use href="#badge-base"/><circle cx="42" cy="27" r="8" fill="none" stroke="var(--teal)" stroke-width="2"/><path d="M38 27 l3 3 l7 -8" fill="none" stroke="var(--teal)" stroke-width="2.2"/></svg>
  <div class="badge-label">Council<br>Approval</div>
</div>

<svg class="abs flow-arrow" style="left:652px" viewBox="0 0 30 22"><path d="M0 7 H16 V0 L30 11 L16 22 V15 H0 Z" fill="var(--navy)"/></svg>

<section class="panel teal-panel docs cdc">
  <h3>What documents do I need for a CDC?</h3>
  <ol>
    <li>CDC Application form</li>
    <li>Section 10.7 Certificate for the Site Address. You can purchase this from your local Council and it will tell you if you are eligible for a CDC. This 10.7 Certificate will also notify you if your site is designated as a floodplain, heritage site, slope hazard zone, or acid sulphate soil risk area. This is important as you will need to consult with specific professionals for the approvals if any of these are identified.</li>
    <li>Deposited Plan/88b. This will check if there are any easements around the proposed site.</li>
    <li>Title Search</li>
    <li>Architectural Plans from an architect or a draftsperson</li>
    <li>Local Water Authority Endorsement</li>
    <li>Pool Engineering Drawings</li>
    <li>BASIX Certificate (Building Sustainability Index. This is only required if your pool is over 40,000L capacity</li>
  </ol>
  <div class="note">Additional documents may be requested such as an arborist report, bushfire attack level or a flood certificate depending on your site.</div>
</section>
<div class="badge" style="left:747px;top:139px"><svg viewBox="0 0 84 84"><use href="#badge-doc"/></svg></div>

<svg class="abs flow-arrow" style="left:897px" viewBox="0 0 30 22"><path d="M0 7 H16 V0 L30 11 L16 22 V15 H0 Z" fill="var(--navy)"/></svg>

<section class="panel teal-panel docs da">
  <h3>Documents for a DA approval</h3>
  <ol>
    <li>Statement of Environmental Effect (SEE)</li>
    <li>Site Survey/Plan</li>
    <li>Detailed DA Design Drawings. These should be completed by an architect or draftsperson and include a number of requirements, check with your local Council for what they require.</li>
    <li>Structural Engineers Pool Drawings and Certification</li>
    <li>Builders Home Warranty Insurance</li>
    <li>Copy of payment receipt for Long Service Levy</li>
    <li>Water Authority Tap In Approval</li>
  </ol>
</section>
<div class="badge" style="left:992px;top:139px"><svg viewBox="0 0 84 84"><use href="#badge-doc"/></svg></div>

<div class="abs base-bar"></div>

<section class="panel navy-panel step3">
  <h3>What happens after my pool is installed?</h3>
  <p>When you're fibreglass pool and pool fence is installed, you'll be ready for a pool inspection. This is the last stage of the pool approval journey. An inspector will visit the site and ensure all regulations have been met. The inspector will conduct inspections, measurements, tests, and capture photographs of your pool gates, pool fences, dividing fences utilised as pool fences, and any objects or structures in close proximity to the pool fence.</p>
</section>
<div class="num on-navy" style="left:290px;top:518px">03</div>
<div class="badge" style="left:344px;top:517px">
  <svg viewBox="0 0 84 84"><use href="#badge-base"/><g stroke="var(--navy)" stroke-width="2.4" stroke-linecap="round"><line x1="35" y1="20" x2="49" y2="34"/><line x1="49" y1="20" x2="35" y2="34"/></g><circle cx="35" cy="20" r="2.6" fill="var(--navy)"/></svg>
  <div class="badge-label">Pool<br>Installation</div>
</div>

<div class="abs tab tab-nsw">NSW</div>
<div class="abs tab tab-guide">DESIGN GUIDELINES</div>

<svg class="abs yellow-arrow" viewBox="0 0 52 41"><path d="M0 12 H24 V0 L52 20.5 L24 41 V29 H0 Z" fill="var(--yellow)"/></svg>
<svg class="abs return-line" viewBox="0 0 22 64"><path d="M0 1.5 H19 V62 H6" fill="none" stroke="var(--navy)" stroke-width="2.5"/><path d="M0 62 L8 57 V67 Z" fill="var(--navy)"/></svg>

<div class="abs grid row-a">
  <div class="cell lbl c-t">Legislatio</div>
  <div class="cell lbl c-n">Relocatable Definition</div>
  <div class="cell lbl c-t">Exemptions from Approval</div>
  <div class="cell lbl c-n">Boundary fence as barrier</div>
  <div class="cell lbl c-t">Boundary Offset: Above Ground Coping may encroach.</div>
  <div class="cell lbl c-n">Boundary Offset: Inground</div>
  <div class="cell lbl c-t">Pool Wall as Barrier</div>
  <div class="cell lbl c-n">Build on Easements</div>
  <div class="cell val c-n"></div>
  <div class="cell val c-t">No definitions apply.</div>
  <div class="cell val c-n">Volume &lt;2000L w. lockable lid.</div>
  <div class="cell val c-t">YES. 1800mm high.</div>
  <div class="cell val c-n">1.0m MIN. to waterline. **Pools (structures over 1400mm high require DA)</div>
  <div class="cell val c-t">1.0m MIN. to waterline. Coping may encroach.</div>
  <div class="cell val c-n">NO</div>
  <div class="cell val c-t">NO under CDC (Barrier ok). May be considered under DA- Council specific.</div>
</div>

<div class="abs grid row-b">
  <div class="cell lbl c-t">Support Slabs</div>
  <div class="cell lbl c-n">CPR Signs (add note on plans)</div>
  <div class="cell lbl c-t">Safety Barriers</div>
  <div class="cell lbl c-n">Body of Water as Barrier</div>
  <div class="cell lbl c-t">Lockable Lids</div>
  <div class="cell lbl c-n">Vegetation Near Barriers</div>
  <div class="cell lbl c-t">Doors &amp; Windows</div>
  <div class="cell lbl c-n">Pool Equipment</div>
  <div class="cell val c-n">Slab must be inc. w. permit. Slab specs. required. Steel inspection required.</div>
  <div class="cell val c-t">YES, mandatory. Must be displayed in the immediate vicinity of the pool area and read from a distance of 3m.</div>
  <div class="cell val c-n">AS1926.1-2012 Standard modified: · Can not use pool wall. · Lockable lid, spas only up to 4.0m long. All other NCZ's as per AS1926.1-2012 (Vic).</div>
  <div class="cell val c-t">NO</div>
  <div class="cell val c-n">YES, seated spas only. Not acceptable on swim spas where a person can move around. &lt;2000 L w. lid. No permit req'd. &gt;2000 L. Lid accepted but permit req'd (lid specs req'd, must be capable of being operated by 1 person)</div>
  <div class="cell val c-t">Outside NCZ's.</div>
  <div class="cell val c-n">No doors. Any windows/openings fixed to 100mm MAX. opening.</div>
  <div class="cell val c-t">Outside NCZ's.</div>
</div>

</body>
</html>
```